Flyer-Design für Wartung, Reparatur und Instandhaltung  von Elektroanlagen
Flyer-Design für Wartung, Reparatur und Instandhaltung von Elektroanlagen
Zielgruppe
Wir bieten Wartung, Reparatur und Instandhaltung von Elektro, Lüftung (RLT-Anlagen),
MSR, Heizung und Brandschutz.
Unsere Zielgruppe sind Privatpersonen sowie Gewerbekunden.
Aufgabenstellung
Es sollte ein 2 Seitiger Flyer sein (1 Seiten beidseitig bedruckt),

```html
<!DOCTYPE html>
<html lang="de">
<head>
<meta charset="utf-8">
<title>Haustechnik Brenner – Visitenkarte</title>
<link rel="stylesheet" href="https://fonts.googleapis.com/css2?family=Montserrat:wght@400;500;700;800&display=swap">
<style>
  :root {
    --stage: #cbcbc7;
    --navy: #233f6f;
    --navy-dark: #1f2a55;
    --sky: #0f82c9;
    --paper: #f2f2f0;
    --white: #ffffff;
    --tint: #7f93c2;
  }
  * { box-sizing: border-box; margin: 0; padding: 0; }
  html, body { width: 1200px; height: 750px; overflow: hidden; }
  body {
    background: var(--stage);
    font-family: "Montserrat", sans-serif;
    position: relative;
  }
  .card {
    position: absolute;
    top: 200px;
    width: 540px;
    height: 340px;
    padding: 34px 36px 28px 40px;
    box-shadow: 0 6px 18px rgba(0,0,0,.18);
    overflow: hidden;
  }
  .card--front { left: 30px; background: var(--navy); color: var(--white); }
  .card--back  { left: 630px; background: var(--paper); color: var(--navy-dark); }

  .brand { display: flex; align-items: center; gap: 14px; }
  .brand__mark { width: 44px; height: 44px; background: var(--sky); }
  .brand__name { font-weight: 800; font-size: 30px; letter-spacing: .5px; line-height: 1; }
  .card--front .brand__name { color: var(--white); }
  .card--back .brand__name { color: var(--navy-dark); }

  .services { list-style: none; margin-top: 30px; }
  .services li {
    display: flex; align-items: center; gap: 14px;
    font-weight: 800; font-size: 24px; letter-spacing: 1px; line-height: 1.25;
    text-transform: uppercase;
  }
  .services li::before {
    content: ""; width: 18px; height: 14px; background: var(--sky); flex: none;
  }
  .card--back .services li { color: var(--sky); }
  .services__note {
    font-weight: 500; font-size: 8px; letter-spacing: .5px; line-height: 1.1;
  }

  .phone {
    display: flex; align-items: center; gap: 8px;
    margin: 14px 0 0 80px;
    font-weight: 800; font-size: 26px; letter-spacing: .5px;
  }
  .phone svg { width: 18px; height: 26px; flex: none; }

  .contact { position: absolute; left: 80px; bottom: 26px; font-size: 10.5px; line-height: 1.5; }
  .contact__name { font-weight: 700; }
  .contact__role { color: var(--sky); }
  .card--front .contact__role { color: var(--white); }
  .contact svg { width: 10px; height: 10px; vertical-align: -1px; }
  .contact .icon { fill: var(--sky); }
</style>
</head>
<body>

<section class="card card--front" aria-label="Vorderseite">
  <div class="brand">
    <span class="brand__mark"></span>
    <span class="brand__name">Haustechnik Brenner</span>
  </div>
  <ul class="services">
    <li>MSR <span class="services__note">Mess-, Steuerungs- und<br>Regelungstechnik</span></li>
    <li>Heizung</li>
    <li>Brandschutz</li>
  </ul>
  <p class="phone">
    <svg viewBox="0 0 18 26" fill="none" stroke="#0f82c9" stroke-width="2.5"><rect x="1.5" y="1.5" width="15" height="23" rx="2.5"/></svg>
    0151-47 83 26 50
  </p>
  <div class="contact">
    <p><span class="contact__name">Markus Feldner</span> | <span class="contact__role">Inhaber / Elektromeister</span></p>
    <p><svg viewBox="0 0 10 10"><path class="icon" d="M5 0 10 5H8.5V10H1.5V5H0Z"/></svg> Am Mühlenweg 12 | 54290 Talheim
      <svg viewBox="0 0 10 10"><path class="icon" d="M0 2H10V9H0ZM0 2 5 6 10 2"/></svg> info@htbrenner.de |
      <svg viewBox="0 0 10 10"><circle class="icon" cx="5" cy="5" r="5"/></svg> www.htbrenner.de</p>
  </div>
</section>

<section class="card card--back" aria-label="Rückseite">
  <div class="brand">
    <span class="brand__mark"></span>
    <span class="brand__name">Haustechnik Brenner</span>
  </div>
  <ul class="services">
    <li>Wartung</li>
    <li>Reparatur</li>
    <li>Instandsetzung</li>
  </ul>
  <p class="phone">
    <svg viewBox="0 0 18 26" fill="none" stroke="#1f2a55" stroke-width="2.5"><rect x="1.5" y="1.5" width="15" height="23" rx="2.5"/></svg>
    0151-47 83 26 50
  </p>
  <div class="contact">
    <p><span class="contact__name">Markus Feldner</span> | <span class="contact__role">Inhaber / Elektromeister</span></p>
    <p><svg viewBox="0 0 10 10"><path class="icon" d="M5 0 10 5H8.5V10H1.5V5H0Z"/></svg> Am Mühlenweg 12 | 54290 Talheim
      <svg viewBox="0 0 10 10"><path class="icon" d="M0 2H10V9H0ZM0 2 5 6 10 2"/></svg> info@htbrenner.de |
      <svg viewBox="0 0 10 10"><circle class="icon" cx="5" cy="5" r="5"/></svg> www.htbrenner.de</p>
  </div>
</section>

</body>
</html>
```